Business Card, Envelopes,Letterhead for Steadfast Blaze Supply
Business Card, Envelopes,Letterhead
Business Card, Envelopes,Letterhead for Steadfast Blaze Supply -
Creative Brief
Use specific fonts
we are open for ideas
Professional
Mark Haverty
47 Corwin Rd. Waukegan illinois, 60085
847-319-5726 x214
mark@steadfastblaze.example
www.steadfastblaze.example
Id like to see all of my logos utilized through out this project-We are a fire safety company that specilizes in inspecting, servicing selling and certifiying FIRE EXTINGUISHERS RESTAURANT SUPPRESSION SYSTEMS EXIT AND EMERGENCY LIGHTING FIRE ALARMS FIRE SPRINKLERS we have 2 locations- main office/shop-47 Corwin Road Harlow Falls, IL 60411 satelite office- 2917 South Tillman Ave. Chicago Illinois 60603

```html
<!DOCTYPE html>
<html lang="en">
<head>
<meta charset="utf-8">
<title>Steadfast Blaze Supply – Stationery Set</title>
<link href="https://fonts.googleapis.com/css2?family=Roboto+Slab:wght@800&family=Open+Sans:wght@400;600;700&display=swap" rel="stylesheet">
<style>
:root{
  --red:#d6262b;
  --orange:#f39a1f;
  --yellow:#fbc02d;
  --ink:#1b1b1b;
  --grey:#6b6b6b;
  --line:#c9c9c9;
  --paper:#ffffff;
  --stage:#ecebe8;
}
*{margin:0;padding:0;box-sizing:border-box}
html,body{width:1200px;height:526px;overflow:hidden;background:var(--stage);font-family:"Open Sans",sans-serif;color:var(--ink)}
.canvas{position:relative;width:1200px;height:526px}
.sheet{position:absolute;background:var(--paper);box-shadow:0 2px 6px rgba(0,0,0,.18);overflow:hidden}
.brand{display:flex;align-items:center;gap:5px}
.brand-dot{border-radius:50%;background:var(--red);flex:none}
.brand-name{font-family:"Roboto Slab",serif;font-weight:800;color:var(--red);line-height:1;text-transform:uppercase;white-space:nowrap}
.small{font-size:5px;color:var(--grey);line-height:1.45}

/* letterhead */
.letterhead{left:43px;top:19px;width:293px;height:468px}
.letterhead .brand{position:absolute;left:18px;top:16px}
.letterhead .brand-dot{width:20px;height:20px}
.letterhead .brand-name{font-size:9px}
.letterhead .watermark{position:absolute;left:62px;top:130px;width:170px;height:170px;border-radius:50%;background:var(--orange);opacity:.12}
.letterhead .footer{position:absolute;left:0;right:0;bottom:14px;text-align:center}

/* fax */
.fax{left:384px;top:29px;width:307px;height:451px}
.fax .brand{position:absolute;left:18px;top:16px}
.fax .brand-dot{width:18px;height:18px}
.fax .brand-name{font-size:8px}
.fax .contact{position:absolute;right:16px;top:14px;text-align:left}
.fax h1{position:absolute;left:18px;top:72px;font-size:20px;font-weight:400;letter-spacing:1px}
.fax .fields{position:absolute;left:18px;top:108px;width:271px;display:grid;grid-template-columns:1fr 1fr;column-gap:14px}
.fax .field{font-size:5px;border-bottom:1px solid var(--line);height:15px;padding-top:6px;color:var(--grey)}
.fax .checks{position:absolute;left:18px;top:200px;width:271px;display:flex;justify-content:space-between}
.fax .check{display:flex;align-items:center;gap:3px;font-size:5px;color:var(--grey)}
.fax .check i{width:6px;height:6px;border:1px solid var(--grey);display:block}
.fax .rule{position:absolute;left:18px;right:18px;top:218px;border-top:1px solid var(--line)}
.wave{position:absolute;left:0;bottom:0;width:100%}

/* envelopes */
.env-back{left:744px;top:29px;width:432px;height:151px}
.env-back .flap{position:absolute;left:0;top:0;width:100%;height:100%}
.env-back .brand{position:absolute;left:50%;top:16px;transform:translateX(-50%)}
.env-back .brand-dot{width:18px;height:18px}
.env-front{left:763px;top:139px;width:360px;height:216px}
.env-front .brand{position:absolute;left:16px;top:14px}
.env-front .brand-dot{width:16px;height:16px}
.env-front .brand-name{font-size:7px}
.env-front .return{position:absolute;left:120px;top:16px}
.env-front .web{position:absolute;right:120px;bottom:14px;font-size:5px;color:var(--paper);z-index:2}

/* business cards */
.card{width:162px;height:80px}
.card-logo{left:768px;top:365px}
.card-logo .brand{position:absolute;left:16px;top:24px}
.card-logo .brand-dot{width:22px;height:22px}
.card-logo .brand-name{font-size:9px}
.card-info{left:953px;top:365px}
.card-info .brand{position:absolute;left:10px;top:9px}
.card-info .brand-dot{width:12px;height:12px}
.card-info .brand-name{font-size:6px}
.card-info .person{position:absolute;left:10px;top:36px;font-size:6.5px;font-weight:700}
.card-info .details{position:absolute;left:10px;top:46px;font-size:4.5px}
.card-info .bar{position:absolute;left:0;right:0;bottom:0;height:5px;background:linear-gradient(90deg,var(--red),var(--orange),var(--yellow))}
.card-dark{left:960px;top:456px;width:168px;height:60px;background:var(--ink)}
.card-dark .brand{position:absolute;left:10px;top:18px}
.card-dark .brand-dot{width:16px;height:16px}
.card-dark .brand-name{font-size:6px}
.card-dark .details{position:absolute;right:10px;top:14px;font-size:4.5px;color:#cfcfcf;text-align:right;line-height:1.5}

.option{position:absolute;top:500px;font-size:13px;font-weight:700;color:var(--ink)}
.option-1{left:150px}
.option-2{left:530px}
</style>
</head>
<body>
<main class="canvas">

  <section class="sheet letterhead" aria-label="Letterhead">
    <div class="brand"><span class="brand-dot"></span><span class="brand-name">Steadfast Blaze<br>Supply</span></div>
    <div class="watermark" aria-hidden="true"></div>
    <p class="footer small">47 Corwin Rd. Harlow Falls, IL 60411 &nbsp;•&nbsp; 847-319-5726 x214 &nbsp;•&nbsp; www.steadfastblaze.example</p>
  </section>

  <section class="sheet fax" aria-label="Fax cover sheet">
    <div class="brand"><span class="brand-dot"></span><span class="brand-name">Steadfast Blaze<br>Supply</span></div>
    <p class="contact small">47 Corwin Rd. Harlow Falls, IL 60411<br>847-319-5726 x214<br>mark@steadfastblaze.example<br>www.steadfastblaze.example</p>
    <h1>FAX</h1>
    <div class="fields">
      <div class="field">To:</div><div class="field">From:</div>
      <div class="field">Fax:</div><div class="field">Pages:</div>
      <div class="field">Phone:</div><div class="field">Date:</div>
      <div class="field">Re:</div><div class="field">CC:</div>
    </div>
    <div class="checks">
      <span class="check"><i></i>Urgent</span>
      <span class="check"><i></i>For Review</span>
      <span class="check"><i></i>Please Comment</span>
      <span class="check"><i></i>Please Reply</span>
      <span class="check"><i></i>Please Recycle</span>
    </div>
    <div class="rule"></div>
    <svg class="wave" viewBox="0 0 307 60" preserveAspectRatio="none" height="60" aria-hidden="true">
      <path d="M0 22 C90 50 200 0 307 18 L307 60 L0 60Z" fill="var(--yellow)"/>
      <path d="M0 32 C100 58 210 8 307 28 L307 60 L0 60Z" fill="var(--orange)"/>
    </svg>
  </section>

  <section class="sheet env-back" aria-label="Envelope back">
    <svg class="flap" viewBox="0 0 432 151" preserveAspectRatio="none" aria-hidden="true">
      <path d="M0 0 L432 0 L432 22 L216 75 L0 22Z" fill="var(--ink)"/>
    </svg>
    <div class="brand"><span class="brand-dot"></span></div>
  </section>

  <section class="sheet env-front" aria-label="Envelope front">
    <div class="brand"><span class="brand-dot"></span><span class="brand-name">Steadfast Blaze<br>Supply</span></div>
    <p class="return small">47 Corwin Rd.<br>Harlow Falls, IL 60411<br>2917 South Tillman Ave. Brookvale</p>
    <svg class="wave" viewBox="0 0 360 56" preserveAspectRatio="none" height="56" aria-hidden="true">
      <path d="M0 20 C110 52 240 0 360 14 L360 56 L0 56Z" fill="var(--yellow)"/>
      <path d="M0 30 C120 58 250 8 360 24 L360 56 L0 56Z" fill="var(--orange)"/>
    </svg>
    <p class="web">www.steadfastblaze.example</p>
  </section>

  <section class="sheet card card-logo" aria-label="Business card front">
    <div class="brand"><span class="brand-dot"></span><span class="brand-name">Steadfast Blaze<br>Supply</span></div>
  </section>

  <section class="sheet card card-info" aria-label="Business card back">
    <div class="brand"><span class="brand-dot"></span><span class="brand-name">Steadfast Blaze<br>Supply</span></div>
    <p class="person">Mark Haverty</p>
    <p class="details small">47 Corwin Rd. Harlow Falls, IL 60411<br>847-319-5726 x214<br>mark@steadfastblaze.example</p>
    <div class="bar"></div>
  </section>

  <section class="sheet card-dark" aria-label="Business card dark version">
    <div class="brand"><span class="brand-dot"></span><span class="brand-name">Steadfast Blaze<br>Supply</span></div>
    <p class="details">Mark Haverty<br>847-319-5726 x214<br>mark@steadfastblaze.example<br>www.steadfastblaze.example</p>
  </section>

  <p class="option option-1">Option_1</p>
  <p class="option option-2">Option_2</p>
</main>
</body>
</html>
```